Simple AD for Digital Publication

Total Size 5" x 5", may include boarder or not
Image Provided; crop or use as background
Incorporate Logo and text as provided

Target Market(s)

Sound Contractors / Integrators

Industry/Entity Type

Audio Video Lighting

Requirements
Must have
• Bold Look that reflects our brand. see website: tovermundic.com - cohesive text and style

```html
<!DOCTYPE html>
<html lang="en">
<head>
<meta charset="utf-8">
<title>Tovermundic Co – Protect &amp; Conceal</title>
<link rel="stylesheet" href="https://fonts.googleapis.com/css2?family=Source+Sans+3:ital,wght@0,600;0,700;0,800;1,700&display=swap">
<style>
  :root {
    --brand-red: #a61e22;
    --white: #ffffff;
    --ink-grey: #3c3c3e;
    --photo-dark: #2a3a22;
    --photo-wood: #b9a48e;
    --photo-glow: #f2c879;
  }
  * { margin: 0; padding: 0; box-sizing: border-box; }
  html, body { width: 1200px; height: 1200px; overflow: hidden; background: var(--white); }
  .ad {
    position: relative;
    width: 1200px;
    height: 1200px;
    background: var(--white);
    font-family: "Source Sans 3", "Myriad Pro", Arial, sans-serif;
    overflow: hidden;
  }
  .hero-photo {
    position: absolute;
    left: 0; top: 0;
    width: 1200px; height: 822px;
    background:
      radial-gradient(ellipse 70% 30% at 55% 18%, rgba(242,200,121,0.55), rgba(242,200,121,0) 70%),
      linear-gradient(180deg, var(--photo-dark) 0%, #3f4a2c 28%, #8f7a64 40%, var(--photo-wood) 60%, #a8927c 100%);
  }
  .headline-panel {
    position: absolute;
    left: 59px; top: 674px;
    width: 874px; height: 343px;
    background: var(--brand-red);
    color: var(--white);
  }
  .headline-word {
    position: absolute;
    font-weight: 700;
    font-size: 112px;
    line-height: 1;
    letter-spacing: -1px;
  }
  .headline-word--protect { left: 66px; top: 20px; }
  .headline-word--conceal { left: 350px; top: 134px; }
  .headline-amp {
    position: absolute;
    left: 444px; top: 100px;
    font-weight: 600;
    font-style: italic;
    font-size: 62px;
    line-height: 1;
  }
  .headline-sub {
    position: absolute;
    left: 60px; top: 262px;
    font-weight: 700;
    font-size: 40px;
    line-height: 1;
    letter-spacing: 0.3px;
  }
  .brand {
    position: absolute;
    left: 61px; top: 1052px;
    display: flex;
    align-items: center;
    gap: 22px;
  }
  .brand-square {
    width: 96px; height: 96px;
    background: var(--ink-grey);
    flex: none;
  }
  .brand-text { display: flex; flex-direction: column; }
  .brand-name {
    color: var(--brand-red);
    font-weight: 800;
    font-size: 66px;
    line-height: 0.95;
    letter-spacing: -0.5px;
  }
  .brand-tagline {
    color: var(--ink-grey);
    font-weight: 700;
    font-style: italic;
    font-size: 32px;
    line-height: 1.1;
    margin-top: 4px;
  }
  .dealer-badge {
    position: absolute;
    left: 969px; top: 1017px;
    width: 205px; height: 133px;
  }
  .dealer-badge-shape { position: absolute; inset: 0; }
  .dealer-badge-label {
    position: absolute;
    left: 0; right: 0; top: 10px;
    text-align: center;
    color: var(--white);
    font-weight: 700;
    font-size: 23px;
    line-height: 1;
  }
  .dealer-badge-icon {
    position: absolute;
    left: 48px; top: 48px;
    width: 110px; height: 60px;
    background: var(--white);
    border-radius: 30px;
  }
  .dealer-badge-cta {
    position: absolute;
    left: 969px; top: 1158px;
    width: 205px;
    text-align: center;
    color: var(--brand-red);
    font-weight: 700;
    font-style: italic;
    font-size: 20px;
    line-height: 1;
  }
</style>
</head>
<body>
  <main class="ad">
    <div class="hero-photo" role="img" aria-label="Photo of a black metal stage floor pocket set into a wooden floor with cables running out of it, with a lit holiday garland of warm string lights behind"></div>

    <section class="headline-panel">
      <h1>
        <span class="headline-word headline-word--protect">Protect</span>
        <span class="headline-amp">&amp;</span>
        <span class="headline-word headline-word--conceal">Conceal</span>
      </h1>
      <p class="headline-sub">High and Low Voltage Connectivity</p>
    </section>

    <div class="brand">
      <div class="brand-square" aria-hidden="true"></div>
      <div class="brand-text">
        <span class="brand-name">TOVERMUNDIC CO</span>
        <span class="brand-tagline">Stage Pocket Systems Connectivity</span>
      </div>
    </div>

    <a class="dealer-badge" href="https://tovermundic.com" aria-label="Become a Dealer">
      <svg class="dealer-badge-shape" viewBox="0 0 205 133" aria-hidden="true">
        <path d="M0 0 H205 V72 Q205 133 140 133 H0 Z" fill="var(--brand-red)"/>
      </svg>
      <span class="dealer-badge-label">Become a Dealer</span>
      <span class="dealer-badge-icon" role="img" aria-label="Handshake icon"></span>
    </a>
    <p class="dealer-badge-cta">(click here)</p>
  </main>
</body>
</html>
```